Infographic Business Process Flowchart

Hi there, I need an infographic designed of one of our company process. We have had someone design something already but we weren't happy with it. Could you please let me know if you could design this? The information we need designed is in the PDF attachment "VelmoPath - One Page". The rest are examples of other flowchart infographics we like. Thanks!

Target Market(s)

Internal company

Industry/Entity Type

Tech

Font styles to use
Sans Serif

Colors

Designer to choose colors to be used in the design.

Requirements
Must have
• Information from "VelmoPath - One Page" document
• Style like one of the samples sent
Nice to have
• Company colours which can be found at velmorix.example

```html
<!DOCTYPE html>
<html lang="en">
<head>
<meta charset="utf-8">
<title>VelmoPath – Project Delivery Process</title>
<link rel="stylesheet" href="https://fonts.googleapis.com/css2?family=Open+Sans:wght@400;600;700&display=swap">
<style>
:root{
  --blue-dark:#1f3ca0;
  --blue:#2f66d6;
  --blue-light:#5fa3ef;
  --green-dark:#1f8a2c;
  --green:#3cb83d;
  --orange:#f0a04d;
  --orange-light:#f6c062;
  --purple:#6a2fb0;
  --red:#c00d0d;
  --ink:#1c1c1c;
  --line:#333;
  --white:#fff;
}
*{box-sizing:border-box;margin:0;padding:0}
html,body{width:848px;height:1200px;overflow:hidden;background:var(--white)}
body{font-family:"Open Sans",Arial,sans-serif;color:var(--ink);position:relative}
.canvas{position:relative;width:848px;height:1200px;overflow:hidden}
.backdrop{position:absolute;left:0;top:0}
.heading{position:absolute;top:34px;font-size:11px;font-weight:700}
.heading.activity{left:101px}
.heading.systems{left:492px}
.row{position:absolute;left:0;width:848px}
.step{position:absolute;left:20px;width:62px;height:58px;color:var(--white);font-size:7.4px;text-align:center;line-height:1.25;display:flex;align-items:center;justify-content:center;padding:10px 3px 8px;
  clip-path:polygon(0 0,50% 16%,100% 0,100% 78%,50% 100%,0 78%)}
.step.blue{background:linear-gradient(180deg,var(--blue-light),var(--blue-dark))}
.step.green{background:linear-gradient(180deg,var(--green),var(--green-dark))}
.step.orange{background:linear-gradient(180deg,var(--orange-light),var(--orange))}
.step.tall{height:66px}
.box{position:absolute;background:var(--white);border:1px solid var(--line);font-size:6px;line-height:1.35;padding:3px 4px;display:flex;flex-direction:column;justify-content:center}
.box.owner{left:96px;width:162px}
.box.task{left:292px;width:162px;justify-content:flex-start;font-size:5.4px;line-height:1.3}
.box.system{left:489px;width:180px}
.tag{position:absolute;left:81px;width:64px;height:22px;background:linear-gradient(90deg,var(--blue-light),var(--blue));color:var(--white);font-size:7.2px;display:flex;align-items:center;justify-content:center}
.banner{position:absolute;left:164px;width:290px;height:24px;background:linear-gradient(90deg,var(--blue-dark),var(--blue-light));color:var(--white);font-size:9px;line-height:1.1;padding:0 12px;display:flex;align-items:center;white-space:nowrap}
.banner.wrap{white-space:normal}
.track{position:absolute;top:368px;height:328px;width:24px;color:var(--white);font-size:6px;display:flex;align-items:center;justify-content:center}
.track span{transform:rotate(-90deg);white-space:nowrap}
.track.time{left:674px;background:var(--orange)}
.track.collab{left:704px;background:var(--purple)}
.track.control{left:733px;background:var(--red)}
.governance{position:absolute;left:760px;top:368px;width:88px;height:210px;background:linear-gradient(180deg,#6fa6f0,#dfe9fb 45%,rgba(255,255,255,0));font-size:5.8px;line-height:1.35;padding:4px 3px}
.governance p{margin-bottom:4px}
.celebrate{position:absolute;left:340px;top:684px;width:62px;height:40px;background:var(--purple);color:var(--white);font-size:6.6px;text-align:center;line-height:1.25;display:flex;align-items:center;justify-content:center;padding-top:2px;
  clip-path:polygon(0 0,50% 14%,100% 0,100% 80%,50% 100%,0 80%)}
.illustration{position:absolute}
.illustration.inspector{left:535px;top:627px;width:313px;height:290px;background:radial-gradient(ellipse at 45% 40%,rgba(70,80,110,.35),rgba(120,150,220,.12) 60%,rgba(255,255,255,0) 75%)}
.illustration.team{left:207px;top:916px;width:641px;height:284px;background:radial-gradient(ellipse at 60% 55%,rgba(255,190,80,.35),rgba(90,110,220,.2) 55%,rgba(255,255,255,0) 80%)}
</style>
</head>
<body>
<div class="canvas">
  <svg class="backdrop" width="848" height="1200" viewBox="0 0 848 1200" aria-hidden="true">
    <defs>
      <linearGradient id="topWash" x1="0" y1="1" x2="1" y2="0">
        <stop offset="0" stop-color="#a9c8f7"/>
        <stop offset=".45" stop-color="#4f7fe0"/>
        <stop offset="1" stop-color="#23338f"/>
      </linearGradient>
      <linearGradient id="bottomWash" x1="0" y1="0" x2="1" y2="0">
        <stop offset="0" stop-color="#f0587a"/>
        <stop offset=".5" stop-color="#b05fc8"/>
        <stop offset="1" stop-color="#6c66e8"/>
      </linearGradient>
    </defs>
    <path d="M420 0 H848 V360 C790 380 740 330 700 300 C640 255 560 300 520 260 C480 220 500 150 470 110 C440 70 380 60 420 0 Z" fill="url(#topWash)"/>
    <path d="M0 1010 C60 960 140 980 200 1000 C280 1025 340 960 420 950 C520 940 560 1010 650 1000 C740 990 790 930 848 920 V1200 H0 Z" fill="url(#bottomWash)"/>
    <circle cx="820" cy="1010" r="70" fill="#5a6fe0" opacity=".6"/>
  </svg>

  <div class="illustration inspector" role="img" aria-label="Illustration of a person holding a large magnifying glass"></div>
  <div class="illustration team" role="img" aria-label="Illustration of a team working at laptops with chat bubbles"></div>

  <div class="heading activity">Activity</div>
  <div class="heading systems">Systems</div>

  <div class="row" style="top:58px">
    <div class="step blue">Create Opportunity</div>
    <div class="tag" style="top:16px">Sales Team</div>
    <div class="banner" style="top:16px">Sales Team Creates an Opportunity in LinkWorks</div>
    <div class="box system" style="top:6px;height:38px">LinkWorks</div>
  </div>
  <svg style="position:absolute;left:146px;top:80px" width="12" height="62" viewBox="0 0 12 62" aria-hidden="true">
    <path d="M1 2 C7 2 5 30 11 31 C5 32 7 60 1 60" fill="none" stroke="#2f66d6" stroke-width="1.4"/>
  </svg>

  <div class="row" style="top:118px">
    <div class="step blue">Convert to Sales Order</div>
    <div class="tag" style="top:12px">Sales Team</div>
    <div class="banner" style="top:2px;width:306px;font-size:7.8px;padding:0 8px;background:linear-gradient(90deg,#2f55c8,#7aaef2)">Operation won opportunities &nbsp; converts &nbsp;are &nbsp;converts it to a Sales Order</div>
    <div class="box system" style="top:0;height:38px">LinkWorks</div>
  </div>

  <div class="row" style="top:154px">
    <div class="step blue">Create Project Template</div>
    <div class="tag" style="top:12px;height:26px;line-height:1.1;text-align:center">Operations<br>Team</div>
    <div class="banner wrap" style="top:12px;height:26px;background:linear-gradient(90deg,#3a6fd8,#8cb8f4)">Operation converts the Sales order to a Project in LinkWorks</div>
    <div class="box system" style="top:6px;height:34px">LinkWorks</div>
  </div>

  <div class="row" style="top:203px">
    <div class="step orange tall">Contact Client</div>
    <div class="box owner" style="top:0;height:42px">Services / (I believe this could be operations, Quinn?)</div>
    <div class="box task" style="top:0;height:42px">Services contact client to acknowledge opportunity and advise of process (This could be automated by Operations / For bigger projects Mara can contact them) – Sales provides contact name, project high level summary</div>
    <div class="box system" style="top:0;height:42px">Email or In person for &gt; 100K projects</div>
  </div>

  <div class="row" style="top:260px">
    <div class="step green">Assign PM</div>
    <div class="box owner" style="top:0;height:40px">Services - PMO</div>
    <div class="box task" style="top:0;height:40px;justify-content:center">Services assign project manager</div>
    <div class="box system" style="top:0;height:40px">Project Manager Capacity Sheet</div>
  </div>

  <div class="row" style="top:310px">
    <div class="step green">Create Team Site</div>
    <div class="box owner" style="top:0;height:42px">Services - PMO</div>
    <div class="box task" style="top:0;height:42px">Services creates HuddleSpace channel for Project under client site<br>Project channel contains templates for project management and checklist for different phases of the engagement</div>
    <div class="box system" style="top:0;height:42px">HuddleSpace</div>
  </div>

  <div class="row" style="top:361px">
    <div class="step green">Initiation</div>
    <div class="box owner" style="top:0;height:46px">Services – PMO &amp; Project</div>
    <div class="box task" style="top:0;height:46px">Project Manager and Sales Handover<br>Project Manager and Practice define team<br>Internal Kick off<br>Pre Client Kick off<br>Client Kick off</div>
    <div class="box system" style="top:0;height:46px">PlanDesk, HuddleSpace, LinkWorks</div>
  </div>

  <div class="row" style="top:418px">
    <div class="step green tall">Planning</div>
    <div class="box owner" style="top:0;height:64px">Services – PMO &amp; Project Team</div>
    <div class="box task" style="top:0;height:64px">Gather Requirements<br>Create WBS<br>Schedule Resources<br>Highlight RAID<br>Refine SoW<br>Refine Project Plan<br>Commitment and Acceptance of Requirements</div>
    <div class="box system" style="top:0;height:64px;justify-content:flex-start">PlanDesk<br>Workshop Templates in HuddleSpace<br>User Stories in TrackLoop / Nimbus DevOps<br>LinkWorks</div>
  </div>

  <div class="row" style="top:491px">
    <div class="step green tall">Execution</div>
    <div class="box owner" style="top:0;height:66px">Services – PMO &amp; Project Team</div>
    <div class="box task" style="top:0;height:66px">Build the various aspects of a solution in accordance with Plan Track deliverables, such as designs, plans, schedules, and requirements and maintain:<br><br>Release Notes<br>Test Results<br>Source Code<br>Project Documentation</div>
    <div class="box system" style="top:0;height:66px">PlanDesk<br>Dev Ops / TrackLoop<br>LinkWorks</div>
  </div>

  <div class="row" style="top:572px">
    <div class="step green tall">Closure</div>
    <div class="box owner" style="top:0;height:64px">Services – PMO &amp; Project Team</div>
    <div class="box task" style="top:0;height:64px">Customer Acceptance<br>Project Close out &amp; Support Planning<br>Performance Review<br>Lessons Learnt<br>IP Session</div>
    <div class="box system" style="top:0;height:40px">HuddleSpace<br>LinkWorks<br>Dev Ops / TrackLoop</div>
  </div>

  <div class="row" style="top:640px">
    <div class="step green tall">Lessons Learnt</div>
    <div class="box owner" style="top:0;height:65px">Services – PMO &amp; Practice</div>
    <div class="box task" style="top:0;height:65px;justify-content:center">What Went Well &amp; What Didn't<br>IP?</div>
    <div class="box system" style="top:0;height:65px">HuddleSpace at Project Level<br>ShareHub at Offering / Service Level</div>
  </div>

  <div class="track time"><span>Time Sheets in LinkWorks</span></div>
  <div class="track collab"><span>Project Collaboration in HuddleSpace</span></div>
  <div class="track control"><span>Control and Governance</span></div>
  <div class="governance">
    <p>Team<br>Services</p>
    <p>Action:</p>
    <p>Stakeholder management through routine project status meeting</p>
    <p>Provide Budget update to client</p>
    <p>Routine meeting with Team to highlight risks and mitigation plans</p>
    <p>Identify opportunities</p>
    <p>Apply technical governance process</p>
    <p>Systems<br>LinkWorks<br>PlanDesk<br>HuddleSpace</p>
  </div>
  <div class="celebrate">Celebrate<br>Success</div>

  <div class="row" style="top:742px">
    <div class="step blue">Support</div>
    <div class="box owner" style="top:2px;height:40px">Services / Managed Services</div>
    <div class="box task" style="top:2px;height:40px;justify-content:center">TBD</div>
    <div class="box system" style="top:2px;height:40px">Support Tickets in LinkWorks</div>
  </div>

  <div class="row" style="top:793px">
    <div class="step blue">Customer Satisfaction</div>
    <div class="box owner" style="top:2px;height:40px">Operations \ Sales</div>
    <div class="box task" style="top:2px;height:40px;justify-content:center">Operations sends Customer Satisfaction survey</div>
    <div class="box system" style="top:2px;height:40px">Forms</div>
  </div>

  <div class="row" style="top:843px">
    <div class="step blue">Project Based Performance</div>
    <div class="box owner" style="top:2px;height:40px">Operations</div>
    <div class="box task" style="top:2px;height:40px;justify-content:center">Operations conducts review on project with practice and PMO team</div>
    <div class="box system" style="top:2px;height:40px">Forms?</div>
  </div>

  <div class="row" style="top:892px">
    <div class="step blue">Case Study</div>
    <div class="box owner" style="top:2px;height:40px">Marketing</div>
    <div class="box task" style="top:2px;height:40px;justify-content:center">Marketing Compiles a Case Study on the project</div>
    <div class="box system" style="top:2px;height:40px">?</div>
  </div>

  <div class="row" style="top:943px">
    <div class="step blue">Support</div>
    <div class="box owner" style="top:2px;height:42px">Services \ Managed Services</div>
    <div class="box task" style="top:2px;height:42px">Ensure support continues in a seamless fashion from one agreement to the next<br>Monthly Report showing the calls managed during the period and including those opened and closed over the period</div>
    <div class="box system" style="top:2px;height:42px">LinkWorks</div>
  </div>

  <div class="row" style="top:1050px">
    <div class="step blue">Human Resource</div>
    <div class="box owner" style="top:2px;height:40px">Operations</div>
    <div class="box task" style="top:2px;height:40px">Recruitment<br>Staff Assessments and Training<br>WHS&amp;S<br>Payroll including Reimbursements</div>
    <div class="box system" style="top:2px;height:40px">LinkWorks<br>Birch HR<br>Ledgro</div>
  </div>

  <div class="row" style="top:1100px">
    <div class="step blue">Finance / ODS</div>
    <div class="box owner" style="top:2px;height:40px">Operations</div>
    <div class="box task" style="top:2px;height:40px">Invoicing<br>Purchasing<br>Financial Report</div>
    <div class="box system" style="top:2px;height:40px">LinkWorks<br>Ledgro</div>
  </div>
</div>
</body>
</html>
```